Combat Sports news website design

Redesigning our existing website to make it more modern, responsive and suitable for our needs. The design needs to take in to account all aspects of our current website structure and services. View the existing website at https://www.bramblewire.co.nz

Particular attention should be paid to our livestream service, which is growing and needs to be much more user friendly to the current experience.

The homepage, article listings and article pages need designs.

Target Market(s)

Combat sports fans

Industry/Entity Type

Media

Coding

Coded - Design and coding required

Number of Pages Required

5+ page

Font styles to use
Sans Serif

Requirements
Must have
• All the functionality of the existing website must be taken in to account, and improved upon.
New design must incorporate our existing logo/colour scheme as this has only just been designed.

```html
<!DOCTYPE html>
<html lang="en">
<head>
<meta charset="utf-8">
<title>Bramblewire – Combat Sports News</title>
<link href="https://fonts.googleapis.com/css2?family=Open+Sans:wght@400;600;700&display=swap" rel="stylesheet">
<style>
:root{
  --red:#a61d28;
  --red-dark:#8e1520;
  --black:#0b0b0b;
  --white:#fff;
  --grey:#777;
  --line:#e4e4e4;
  --page:#fff;
}
*{box-sizing:border-box;margin:0;padding:0}
html,body{width:1200px;height:2337px;overflow:hidden}
body{position:relative;background:var(--page);font-family:'Open Sans',sans-serif;color:#222}
.abs{position:absolute}
.topbar{left:0;top:0;width:1200px;height:50px;background:var(--red)}
.topbar .info{position:absolute;top:18px;font-size:10.5px;color:#fff;display:flex;gap:5px;align-items:center}
.topbar .links{position:absolute;left:751px;top:18px;display:flex;gap:18px;font-size:10.5px;color:#fff}
.topbar .divider{position:absolute;left:722px;top:14px;width:1px;height:22px;background:rgba(255,255,255,.35)}
.topbar .social{position:absolute;left:956px;top:20px;display:flex;gap:14px}
.dot{width:9px;height:9px;border-radius:50%;background:#fff;display:block}
.search{position:absolute;left:1049px;top:14px;width:23px;height:22px;background:#fff;display:flex;align-items:center;justify-content:center}
.navbar{left:0;top:50px;width:1200px;height:36px;background:var(--black)}
.navbar ul{list-style:none;display:flex;position:absolute;left:311px;top:12px;gap:0}
.navbar li{font-size:10.5px;font-weight:600;color:#fff;margin-right:27px}
.navbar li.active{color:#e0373f;font-weight:400}
.brand{left:128px;top:0;width:120px;height:83px;background:#fff;border-bottom:3px solid var(--red);display:flex;flex-direction:column;align-items:center;justify-content:center;box-shadow:0 2px 4px rgba(0,0,0,.2)}
.brand span{font-weight:700;color:var(--red);font-size:16px;line-height:18px;letter-spacing:.5px}
.banner{left:343px;top:100px;width:514px;height:63px;border:1px solid #e2e2e2;background:#fff}
.banner .mark{position:absolute;left:16px;top:8px;width:47px;height:47px;background:#1b1b1b}
.banner p{position:absolute;left:82px;top:12px;font-size:17px;line-height:19px;color:#555}
.banner .btn{position:absolute;left:374px;top:17px;width:128px;height:28px;background:#333;color:#fff;font-weight:700;font-size:13px;display:flex;align-items:center;justify-content:center}
.slide{top:178px;height:344px;overflow:hidden}
.slide .ph{position:absolute;inset:0}
.slide .cap{position:absolute;left:0;bottom:0;background:var(--red);color:#fff;font-weight:600;font-size:14.5px;line-height:18px;padding:38px 14px 14px}
.slide .cap.dark{background:rgba(0,0,0,.55)}
.pill{position:absolute;background:#fff;height:24px;display:flex;align-items:center;gap:6px;padding:0 12px;font-size:10px;color:#222;white-space:nowrap}
.pill svg{width:11px;height:11px}
.pill .sp{width:14px}
.panel{background:#fff;box-shadow:0 0 6px rgba(0,0,0,.08)}
.phead{position:absolute;left:0;top:0;width:100%;height:34px;background:var(--red);color:#fff;font-weight:600;font-size:12.5px;display:flex;align-items:center;justify-content:center}
.phead::after{content:"";position:absolute;left:50%;bottom:-6px;margin-left:-6px;border:6px solid transparent;border-bottom:0;border-top-color:var(--red)}
.card{position:absolute;background:var(--black);color:#fff}
.card.red{background:var(--red)}
.card .media{position:relative;border-bottom:2px solid var(--red)}
.card.red .media{border-bottom-color:var(--red-dark)}
.card .pill{left:14px;bottom:-10px}
.card h3{font-size:13px;font-weight:700;line-height:17.5px;padding:0 14px}
.card p{font-size:11px;line-height:18px;padding:0 14px;margin-top:13px;color:#eee}
.latest li{list-style:none;position:absolute;left:14px;width:213px;height:91px;border-bottom:1px solid var(--line)}
.latest .th{position:absolute;left:0;top:0;width:62px;height:62px}
.latest .t{position:absolute;left:76px;top:0;font-size:11px;line-height:14px;color:#c62a33;width:135px}
.latest .m{position:absolute;left:76px;top:50px;font-size:9.5px;color:#999}
.adbox{position:absolute;left:18px;top:48px;width:213px;height:176px;border:1px solid #e6e6e6}
.adbox .sq{position:absolute;left:16px;top:22px;width:36px;height:36px;border:3px solid #333;border-radius:50%}
.adbox h4{position:absolute;left:64px;top:20px;font-weight:400;font-size:14px;line-height:18px;color:#333}
.adbox p{position:absolute;left:16px;top:72px;width:185px;font-size:10px;line-height:13.5px;color:#777}
.adbox small{position:absolute;left:16px;top:128px;font-size:9px;color:#aaa}
.adbox .open{position:absolute;left:16px;top:146px;width:181px;height:26px;background:#333;color:#fff;font-size:11px;display:flex;align-items:center;justify-content:center;border-radius:2px}
.adbox .x{position:absolute;right:2px;top:2px;width:18px;height:8px;background:#cfe3ef}
.poll .q{position:absolute;left:14px;top:58px;font-size:12.5px;color:#333}
.opt{position:absolute;left:14px;font-size:12px;color:#333;display:flex;align-items:center;gap:11px}
.opt i{width:12px;height:12px;border:1px solid #bbb;border-radius:50%;display:block;position:relative}
.opt i.on::after{content:"";position:absolute;left:2px;top:2px;width:6px;height:6px;border-radius:50%;background:var(--red)}
.pbtn{position:absolute;top:228px;width:96px;height:28px;background:var(--red);color:#fff;font-size:12px;font-weight:600;display:flex;align-items:center;justify-content:center}
.fbrand{left:542px;top:2175px;width:116px;display:flex;flex-direction:column;align-items:center}
.fbrand span{font-weight:700;color:var(--red);font-size:20px;line-height:23px;letter-spacing:.5px}
.fnav{left:219px;top:2268px;display:flex;font-size:11px;color:#222}
.fnav span{margin-right:27px}
.fnav .active{color:#c62a33}
.fbar{left:0;top:2302px;width:1200px;height:35px;background:var(--red);color:#fff;font-size:11.5px}
.fbar p{position:absolute;left:131px;top:10px}
.fbar .social{position:absolute;left:1015px;top:13px;display:flex;gap:14px}
</style>
</head>
<body>

<header>
  <div class="abs topbar">
    <div class="info" style="left:551px">
      <svg width="11" height="11" viewBox="0 0 12 12"><circle cx="6" cy="6" r="5" fill="none" stroke="#fff" stroke-width="1.4"/><path d="M6 3v3l2 1" stroke="#fff" stroke-width="1.2" fill="none"/></svg>10:17:09
    </div>
    <div class="info" style="left:624px">
      <svg width="11" height="11" viewBox="0 0 12 12"><rect x="1" y="2" width="10" height="9" fill="none" stroke="#fff" stroke-width="1.3"/><path d="M1 5h10" stroke="#fff"/></svg>28 Apr 2021
    </div>
    <div class="divider"></div>
    <div class="links"><span>About</span><span>Advertise</span><span>Contact</span></div>
    <div class="social"><i class="dot"></i><i class="dot"></i><i class="dot"></i></div>
    <div class="search"><svg width="11" height="11" viewBox="0 0 12 12"><circle cx="5" cy="5" r="3.6" fill="none" stroke="var(--red)" stroke-width="1.8"/><path d="M7.6 7.6l3 3" stroke="var(--red)" stroke-width="2"/></svg></div>
  </div>
  <nav class="abs navbar">
    <ul>
      <li class="active">HOME</li><li>MMA</li><li>KICKBOXING</li><li>BOXING</li><li>WRESTLING</li><li>ICF</li><li>ZENITHFC</li><li>LIVE EVENTS</li><li>CONTACT US</li><li>LOGIN</li><li>REGISTER</li>
    </ul>
  </nav>
  <div class="abs brand"><span>BRAMBLE</span><span>WIRE</span></div>
</header>

<aside class="abs banner">
  <div class="mark"></div>
  <p>Bring your business online. Our<br>24/7 guides can help.</p>
  <div class="btn">SHOP NOW</div>
</aside>

<section class="hero">
  <div class="abs slide" style="left:0;width:265px">
    <div class="ph" role="img" aria-label="Two fighters exchanging strikes in the cage" style="background:linear-gradient(135deg,#3a2a22,#120d0b 70%)"></div>
    <div class="cap dark" style="left:-200px;width:258px;padding-top:14px">Unbroken Fight Series 2 results crowned</div>
  </div>
  <div class="abs slide" style="left:279px;width:641px">
    <div class="ph" role="img" aria-label="Group of champions posing with title belts in a gym" style="background:linear-gradient(160deg,#6b4a3c,#2a1f1c 55%,#3a2d2a)"></div>
    <div class="cap" style="width:357px;height:85px">Five KTN New Zealand Cup winners crowned<br>at Fury Night 9</div>
    <div class="pill" style="left:15px;top:250px">
      <svg viewBox="0 0 12 12"><circle cx="6" cy="6" r="5" fill="none" stroke="#c62a33" stroke-width="1.4"/><path d="M6 3v3l2 1" stroke="#c62a33" fill="none"/></svg>14:00<span class="sp"></span>
      <svg viewBox="0 0 12 12"><rect x="1" y="2" width="10" height="9" fill="none" stroke="#c62a33" stroke-width="1.3"/><path d="M1 5h10" stroke="#c62a33"/></svg>Wed 28 Apr
    </div>
  </div>
  <div class="abs slide" style="left:935px;width:265px">
    <div class="ph" role="img" aria-label="Fighters celebrating with belts in the ring" style="background:linear-gradient(160deg,#2a3aa8,#8a2a1c 60%,#20202a)"></div>
    <div class="cap dark" style="width:300px;height:85px;background:rgba(0,0,0,.35)">Hallard predicts hard fight at Summit<br>this Saturday</div>
    <div class="pill" style="left:15px;top:250px">
      <svg viewBox="0 0 12 12"><circle cx="6" cy="6" r="5" fill="none" stroke="#c62a33" stroke-width="1.4"/><path d="M6 3v3l2 1" stroke="#c62a33" fill="none"/></svg>14:00<span class="sp"></span>
      <svg viewBox="0 0 12 12"><rect x="1" y="2" width="10" height="9" fill="none" stroke="#c62a33" stroke-width="1.3"/><path d="M1 5h10" stroke="#c62a33"/></svg>Wed 28 Apr
    </div>
  </div>
</section>

<main>
  <section class="abs panel" style="left:128px;top:561px;width:682px;height:473px">
    <div class="phead">RECENT HEADLINES</div>
    <article class="card" style="left:22px;top:55px;width:380px;height:397px">
      <div class="media" style="height:258px;background:linear-gradient(180deg,#1a2a6a,#2a3f8a 60%,#16224f)" role="img" aria-label="Event poster with four fighters for a muay thai series">
        <div class="pill"><svg viewBox="0 0 12 12"><circle cx="6" cy="6" r="5" fill="none" stroke="#c62a33" stroke-width="1.4"/><path d="M6 3v3l2 1" stroke="#c62a33" fill="none"/></svg>14:00<span class="sp"></span><svg viewBox="0 0 12 12"><rect x="1" y="2" width="10" height="9" fill="none" stroke="#c62a33" stroke-width="1.3"/><path d="M1 5h10" stroke="#c62a33"/></svg>Wed 28 Apr</div>
      </div>
      <h3 style="margin-top:36px">Summit Muay Thai Warrior Series #2<br>this Saturday</h3>
      <p>The second instalment of Summit Muay Thai Warrior Series<br>takes place this Saturday,...</p>
    </article>
    <article class="card red" style="left:423px;top:55px;width:237px;height:188px">
      <div class="media" style="height:99px;background:linear-gradient(135deg,#2a2a2a,#555 50%,#1a1a1a)" role="img" aria-label="Promotional poster of two heavyweight boxers">
        <div class="pill"><svg viewBox="0 0 12 12"><circle cx="6" cy="6" r="5" fill="none" stroke="#c62a33" stroke-width="1.4"/><path d="M6 3v3l2 1" stroke="#c62a33" fill="none"/></svg>14:00<span class="sp"></span><svg viewBox="0 0 12 12"><rect x="1" y="2" width="10" height="9" fill="none" stroke="#c62a33" stroke-width="1.3"/><path d="M1 5h10" stroke="#c62a33"/></svg>Wed 28 Apr</div>
      </div>
      <h3 style="margin-top:26px;font-size:12.5px;line-height:16px">VIDEO: “I’m bringing pain!” - Marcus Delane declares war on Tevita Rowe</h3>
    </article>
    <article class="card" style="left:423px;top:264px;width:237px;height:188px">
      <div class="media" style="height:85px;background:linear-gradient(135deg,#7a2a22,#3a1a16 60%,#111)" role="img" aria-label="Boxers trading punches in the ring">
        <div class="pill"><svg viewBox="0 0 12 12"><circle cx="6" cy="6" r="5" fill="none" stroke="#c62a33" stroke-width="1.4"/><path d="M6 3v3l2 1" stroke="#c62a33" fill="none"/></svg>14:00<span class="sp"></span><svg viewBox="0 0 12 12"><rect x="1" y="2" width="10" height="9" fill="none" stroke="#c62a33" stroke-width="1.3"/><path d="M1 5h10" stroke="#c62a33"/></svg>Wed 28 Apr</div>
      </div>
      <h3 style="margin-top:26px;font-size:12.5px;line-height:16px">Chris Ebbett aims to stay<br>busy in 2021</h3>
    </article>
  </section>

  <section class="abs panel" style="left:128px;top:1056px;width:682px;height:1057px">
    <div class="phead">EARLIER NEWS</div>
    <article class="card" style="left:21px;top:54px;width:309px;height:313px">
      <div class="media" style="height:168px;background:linear-gradient(180deg,#5a5a5a,#2b2b2b 70%,#444)" role="img" aria-label="Bearded fighter in the ring">
        <div class="pill"><svg viewBox="0 0 12 12"><circle cx="6" cy="6" r="5" fill="none" stroke="#c62a33" stroke-width="1.4"/><path d="M6 3v3l2 1" stroke="#c62a33" fill="none"/></svg>14:00<span class="sp"></span><svg viewBox="0 0 12 12"><rect x="1" y="2" width="10" height="9" fill="none" stroke="#c62a33" stroke-width="1.3"/><path d="M1 5h10" stroke="#c62a33"/></svg>Wed 28 Apr</div>
      </div>
      <h3 style="margin-top:28px">Nolan Sheard two-time South Island champ with victory at Cage Clash</h3>
      <p>Nolan Sheard (Strike Lab Queenstown) won the WKSA South Island 84.6kg full Thai rules title last Sat-urday,...</p>
    </article>
    <article class="card" style="left:351px;top:54px;width:309px;height:313px">
      <div class="media" style="height:168px;background:linear-gradient(135deg,#6a7a8a,#2a3038 70%)" role="img" aria-label="Portrait of a reigning middleweight title holder">
        <div class="pill"><svg viewBox="0 0 12 12"><circle cx="6" cy="6" r="5" fill="none" stroke="#c62a33" stroke-width="1.4"/><path d="M6 3v3l2 1" stroke="#c62a33" fill="none"/></svg>14:00<span class="sp"></span><svg viewBox="0 0 12 12"><rect x="1" y="2" width="10" height="9" fill="none" stroke="#c62a33" stroke-width="1.3"/><path d="M1 5h10" stroke="#c62a33"/></svg>Wed 28 Apr</div>
      </div>
      <h3 style="margin-top:28px">Okoro to defend title at ICF 263</h3>
      <p style="margin-top:22px">ICF champion Emeka Okoro is the latest<br>Kiwi announced to fight at ICF 263. Okoro<br>will...</p>
    </article>
    <article class="card" style="left:21px;top:389px;width:309px;height:313px">
      <div class="media" style="height:168px;background:linear-gradient(90deg,#0b0b0b 25%,#6a5a4a 50%,#0b0b0b 78%)" role="img" aria-label="Fighter holding a championship belt">
        <div class="pill"><svg viewBox="0 0 12 12"><circle cx="6" cy="6" r="5" fill="none" stroke="#c62a33" stroke-width="1.4"/><path d="M6 3v3l2 1" stroke="#c62a33" fill="none"/></svg>14:00<span class="sp"></span><svg viewBox="0 0 12 12"><rect x="1" y="2" width="10" height="9" fill="none" stroke="#c62a33" stroke-width="1.3"/><path d="M1 5h10" stroke="#c62a33"/></svg>Wed 28 Apr</div>
      </div>
      <h3 style="margin-top:28px">Dominic Reeve defeats KTN world champ<br>at Fury Night 9</h3>
      <p>South Island Lee Tan's Dominic ‘Iron Wave’ Reeve defeated KTN Featherweight Muay Thai World Champion Sakdaphon...</p>
    </article>
    <article class="card red" style="left:351px;top:389px;width:309px;height:313px">
      <div class="media" style="height:168px;background:linear-gradient(180deg,#1a1a1a,#5a3a2a 60%,#222)" role="img" aria-label="Fight night poster with line-up of fighters">
        <div class="pill"><svg viewBox="0 0 12 12"><circle cx="6" cy="6" r="5" fill="none" stroke="#c62a33" stroke-width="1.4"/><path d="M6 3v3l2 1" stroke="#c62a33" fill="none"/></svg>14:00<span class="sp"></span><svg viewBox="0 0 12 12"><rect x="1" y="2" width="10" height="9" fill="none" stroke="#c62a33" stroke-width="1.3"/><path d="M1 5h10" stroke="#c62a33"/></svg>Wed 28 Apr</div>
      </div>
      <h3 style="margin-top:28px">KMT Fight Night tonight in Hamilton</h3>
      <p style="margin-top:22px">KMT Fight Night brings another night of Muay Thai action this Saturday, April 24 at Kowhai Muay Thai gym in Hamilton....</p>
    </article>
    <article class="card" style="left:21px;top:724px;width:309px;height:313px">
      <div class="media" style="height:168px;background:linear-gradient(135deg,#888,#222 60%,#555)" role="img" aria-label="Black and white photo of a fighter in the cage">
        <div class="pill"><svg viewBox="0 0 12 12"><circle cx="6" cy="6" r="5" fill="none" stroke="#c62a33" stroke-width="1.4"/><path d="M6 3v3l2 1" stroke="#c62a33" fill="none"/></svg>14:00<span class="sp"></span><svg viewBox="0 0 12 12"><rect x="1" y="2" width="10" height="9" fill="none" stroke="#c62a33" stroke-width="1.3"/><path d="M1 5h10" stroke="#c62a33"/></svg>Wed 28 Apr</div>
      </div>
      <h3 style="margin-top:28px">Hayden Tolle with quick turnaround<br>into Summit</h3>
      <p>Hayden 'Far North' Tolle is a veteran of the New Zealand fight game, boasting 53 fights' experience and...</p>
    </article>
  </section>

  <aside>
    <section class="abs panel" style="left:831px;top:561px;width:241px;height:244px">
      <div class="phead">ADVERTISMENT</div>
      <div class="adbox" style="left:17px;top:54px">
        <i class="x"></i><i class="sq"></i>
        <h4>Launch Your<br>Website</h4>
        <p>You'll need: A studio. A second job. And an online store. Launch it with Launchpad.</p>
        <small>Launchpad</small>
        <div class="open">Open</div>
      </div>
    </section>

    <section class="abs panel latest" style="left:831px;top:828px;width:241px;height:542px">
      <div class="phead">LATEST HEADLINES</div>
      <ul>
        <li style="top:59px"><div class="th" role="img" aria-label="Champions with belts" style="background:linear-gradient(135deg,#6b4a3c,#2a1f1c)"></div><div class="t">Five KTN New Zealand Cup winners crowned at Fury Night 9</div><div class="m">14:00 &nbsp;Wed 28</div></li>
        <li style="top:150px"><div class="th" role="img" aria-label="Fighters celebrating" style="background:linear-gradient(135deg,#2a3aa8,#8a2a1c)"></div><div class="t">Hallard predicts hard fight at Summit this Satur-day</div><div class="m">14:00 &nbsp;Wed 28</div></li>
        <li style="top:241px"><div class="th" role="img" aria-label="Cage fight action" style="background:linear-gradient(135deg,#3a2a22,#120d0b)"></div><div class="t">Unbroken Fight Series 2 results</div><div class="m">14:00 &nbsp;Wed 28</div></li>
        <li style="top:332px"><div class="th" role="img" aria-label="Muay thai series poster" style="background:linear-gradient(180deg,#1a2a6a,#2a3f8a)"></div><div class="t">Summit Muay Thai Warrior Series #2 this Saturday</div><div class="m">14:00 &nbsp;Wed 28</div></li>
        <li style="top:423px"><div class="th" role="img" aria-label="Heavyweight boxing poster" style="background:linear-gradient(135deg,#2a2a2a,#555)"></div><div class="t">VIDEO: “I'm bringing pain!” - Marcus Delane declares war on Tevita</div><div class="m">14:00 &nbsp;Wed 28</div></li>
      </ul>
    </section>

    <section class="abs panel" style="left:831px;top:1391px;width:241px;height:245px">
      <div class="phead">ADVERTISMENT</div>
      <div class="adbox" style="left:17px;top:54px">
        <i class="x"></i><i class="sq"></i>
        <h4>Launch Your<br>Website</h4>
        <p>You'll need: A studio. A second job. And an online store. Launch it with Launchpad.</p>
        <small>Launchpad</small>
        <div class="open">Open</div>
      </div>
    </section>

    <section class="abs panel" style="left:831px;top:1658px;width:241px;height:154px">
      <div class="phead">FOLLOW US</div>
      <div style="position:absolute;left:14px;top:54px;width:214px;height:85px;background:linear-gradient(90deg,#111,#2a0d10 60%,#5a1218)" role="img" aria-label="Social page cover banner">
        <div style="position:absolute;left:8px;top:8px;width:28px;height:28px;background:#fff"></div>
        <div style="position:absolute;left:43px;top:7px;color:#fff;font-size:11px">Bramblewire</div>
        <div style="position:absolute;left:43px;top:21px;color:#ddd;font-size:7.5px">9,840 likes</div>
        <div style="position:absolute;left:6px;top:66px;background:#fff;color:#333;font-size:7.5px;padding:2px 6px">Like Page</div>
        <div style="position:absolute;right:6px;top:66px;background:#fff;color:#333;font-size:7.5px;padding:2px 6px">Learn More</div>
      </div>
    </section>

    <section class="abs panel poll" style="left:831px;top:1833px;width:241px;height:280px">
      <div class="phead">OPINION POLL</div>
      <div class="q">What combat sport do you prefer?</div>
      <div class="opt" style="top:89px"><i></i>MMA</div>
      <div class="opt" style="top:115px"><i></i>Wrestling</div>
      <div class="opt" style="top:141px"><i class="on"></i>Kickboxing</div>
      <div class="opt" style="top:167px"><i></i>Muay Thai</div>
      <div class="opt" style="top:193px"><i></i>All of the above</div>
      <div class="pbtn" style="left:14px">Vote</div>
      <div class="pbtn" style="left:124px">View Results</div>
    </section>
  </aside>
</main>

<footer>
  <div class="abs fbrand"><span>BRAMBLE</span><span>WIRE</span></div>
  <div class="abs fnav"><span class="active">HOME</span><span>MMA</span><span>KICKBOXING</span><span>BOXING</span><span>WRESTLING</span><span>ICF</span><span>ZENITHFC</span><span>LIVE EVENTS</span><span>CONTACT US</span><span>LOGIN</span><span>REGISTER</span></div>
  <div class="abs fbar">
    <p>Copyright © 2021 Bramblewire. All Rights Reserved</p>
    <div class="social"><i class="dot"></i><i class="dot"></i><i class="dot"></i></div>
  </div>
</footer>

</body>
</html>
```